Velmora Flowers Florist Flyer

We are requiring a flyer that advertises and promotes our new business. We specialise in weddings and events but would also like to branch out to corporates and an online subscription. Our brand is feminine/romantic with a touch of elegance and luxury. Our main colour schemes are white, black, gold and pale pink. Instagram: Velmora_flowers and website www.velmoraflowers.com.au
Target Market(s)
brides to be, females
Industry/Entity Type
Florist
Font styles to use
Sans Serif
Script
Other font styles liked:
- The Carpenter
Colors
ffffff
000000
333333
Requirements
Must have
- Feminine/romantic feel, through use of theme colours and elegant font
- our contact details Ph: 0478215096
- email address: contactus@velmoraflowers.com.au
Nice to have
- a description of us willing to work with clients to create their dream wedding flowers. That we offer consultations and no obligation quotes.

```html
<!DOCTYPE html>
<html lang="en">
<head>
<meta charset="utf-8">
<title>Velmora Flowers Flyer</title>
<link href="https://fonts.googleapis.com/css2?family=Josefin+Sans:wght@300;400;600&display=swap" rel="stylesheet">
<style>
  :root{
    --bg:#e9e9e9;
    --paper:#ffffff;
    --ink:#1a1a1a;
    --body:#333333;
    --pink:#eaa5ca;
    --pink-deep:#d27aa9;
    --black:#000000;
  }
  *{box-sizing:border-box;margin:0;padding:0}
  html,body{width:1200px;height:1200px;overflow:hidden;background:var(--bg)}
  body{font-family:"Josefin Sans",sans-serif;color:var(--body)}
  .flyer{position:absolute;left:200px;top:35px;width:800px;height:1130px;background:var(--paper);box-shadow:0 6px 24px rgba(0,0,0,.18);overflow:hidden}
  .photo{position:absolute}
  .photo--peach{left:0;top:0;width:240px;height:150px;background:linear-gradient(135deg,#f1d9c8,#d9b49a 60%,#6b5a4c)}
  .photo--red{left:0;top:158px;width:240px;height:302px;background:radial-gradient(circle at 55% 45%,#b8313a 0,#6d7a4e 35%,#3b4a33 60%,#8a8f98 100%)}
  .photo--mauve{left:248px;top:0;width:262px;height:205px;background:radial-gradient(circle at 55% 55%,#e3b7c2,#a48ba6 45%,#4c4a4f 85%)}
  .photo--table{left:248px;top:371px;width:262px;height:89px;background:linear-gradient(180deg,#7d6a56,#e9e3d8 60%,#c8b79c)}
  .photo--white{left:518px;top:0;width:282px;height:300px;background:radial-gradient(circle at 55% 50%,#f4efe6 0,#dfe0dc 40%,#4a4a52 80%)}
  .photo--pink{left:518px;top:308px;width:282px;height:152px;background:radial-gradient(circle at 50% 45%,#f1a7b4,#d47a8c 40%,#8c9a88 70%,#c6c6c6)}
  .brand{position:absolute;left:248px;top:213px;width:262px;height:150px;background:var(--paper);display:flex;align-items:center;justify-content:center;text-align:center}
  .brand__name{font-size:30px;font-weight:400;color:var(--ink);letter-spacing:.04em;line-height:1.2}
  .services{position:absolute;left:0;top:460px;width:800px;height:100px;background:var(--pink)}
  .services__title{position:absolute;left:40px;top:40px;font-size:22px;font-weight:400;color:var(--ink);letter-spacing:.02em}
  .services__list{position:absolute;right:20px;top:14px;display:flex;gap:34px}
  .service{width:70px;text-align:center;font-size:11px;color:var(--ink);letter-spacing:.03em}
  .service svg{width:36px;height:36px;display:block;margin:0 auto 5px}
  .content{position:absolute;left:40px;top:582px;width:720px}
  .heading{font-size:22px;font-weight:400;color:var(--ink);display:inline-block;border-bottom:2px solid var(--pink-deep);padding-bottom:2px;margin-bottom:8px}
  .heading span{color:var(--pink-deep)}
  .about{font-size:11.5px;font-weight:300;line-height:1.45;margin-bottom:22px}
  .reasons{display:grid;grid-template-columns:1fr 1fr;column-gap:40px}
  .reason{margin-top:16px}
  .reason h3{font-size:15px;font-weight:400;color:var(--ink);position:relative;padding-left:12px;margin-bottom:4px}
  .reason h3::before{content:"";position:absolute;left:0;top:5px;width:5px;height:5px;border-radius:50%;background:var(--pink-deep)}
  .reason p{font-size:11px;font-weight:300;line-height:1.45;padding-left:12px}
  .footer{position:absolute;left:0;bottom:0;width:800px;height:72px;background:var(--pink)}
  .contact{position:absolute;display:flex;align-items:center;gap:8px;font-size:16px;font-weight:600;color:var(--ink)}
  .contact svg{width:16px;height:16px}
  .contact--email{left:30px;top:14px}
  .contact--phone{left:300px;top:42px}
  .web{position:absolute;right:0;bottom:0;width:330px;height:56px;background:var(--black);color:#fff;display:flex;align-items:center;justify-content:center;gap:10px;font-size:17px;font-weight:600}
  .web svg{width:16px;height:16px}
</style>
</head>
<body>
<main class="flyer">
  <div class="photo photo--peach" role="img" aria-label="Bouquet of peach roses"></div>
  <div class="photo photo--red" role="img" aria-label="Bouquet of red and white roses with foliage"></div>
  <div class="photo photo--mauve" role="img" aria-label="Bouquet of pink and mauve roses with tulips"></div>
  <div class="photo photo--table" role="img" aria-label="White floral centrepieces at an event table"></div>
  <div class="photo photo--white" role="img" aria-label="Bouquet of white and blush roses"></div>
  <div class="photo photo--pink" role="img" aria-label="Bouquet of pink roses"></div>
  <div class="brand"><p class="brand__name">Velmora Flowers</p></div>

  <section class="services">
    <h2 class="services__title">OUR BEST SERVICES</h2>
    <div class="services__list">
      <div class="service">
        <svg viewBox="0 0 36 36" fill="none" stroke="#1a1a1a" stroke-width="1.6"><rect x="4" y="7" width="28" height="25" rx="2"/><line x1="4" y1="13" x2="32" y2="13"/><line x1="11" y1="4" x2="11" y2="9"/><line x1="25" y1="4" x2="25" y2="9"/><path d="M18 28c-5-3.5-7-6-7-8.3 0-2 1.6-3.3 3.3-3.3 1.6 0 2.9 1.1 3.7 2.3.8-1.2 2.1-2.3 3.7-2.3 1.7 0 3.3 1.3 3.3 3.3 0 2.3-2 4.8-7 8.3z"/></svg>
        WEDDINGS
      </div>
      <div class="service">
        <svg viewBox="0 0 36 36" fill="none" stroke="#1a1a1a" stroke-width="1.6"><rect x="4" y="7" width="28" height="25" rx="2"/><line x1="4" y1="13" x2="32" y2="13"/><line x1="11" y1="4" x2="11" y2="9"/><line x1="25" y1="4" x2="25" y2="9"/><path d="M18 16l2.3 4.6 5 .7-3.6 3.5.9 5-4.6-2.4-4.6 2.4.9-5-3.6-3.5 5-.7z"/></svg>
        EVENTS
      </div>
      <div class="service">
        <svg viewBox="0 0 36 36" fill="none" stroke="#1a1a1a" stroke-width="1.6"><rect x="3" y="11" width="30" height="20" rx="2"/><path d="M13 11V7h10v4"/><line x1="3" y1="19" x2="33" y2="19"/></svg>
        BUSINESS
      </div>
      <div class="service">
        <svg viewBox="0 0 36 36" fill="none" stroke="#1a1a1a" stroke-width="1.6"><path d="M4 17L18 5l14 12"/><path d="M8 14v17h20V14"/><rect x="15" y="21" width="6" height="10"/></svg>
        HOME
      </div>
    </div>
  </section>

  <section class="content">
    <h2 class="heading">ABOUT <span>US</span></h2>
    <p class="about">For generations we've been creating flowers for family and friends. Over the years this has been our test bed for creating our design pieces for weddings and events. Now we want to make our beautiful creations available to everyone. Our designers have had extensive backgrounds, from owning a florist, to chocolate bouquet design and creations. Our friends and family loved working with our designers to create their perfect flower design, no matter what the event was.</p>

    <h2 class="heading">WHY <span>CHOOSE US?</span></h2>
    <div class="reasons">
      <div>
        <article class="reason"><h3>WE'RE CREATIVE</h3><p>With many years of experience behind us and a combined 20 plus years in the industry, we know what we're talking about. We're here to create spectacular floral designs to suit your needs.</p></article>
        <article class="reason"><h3>WE HAVE YOU FRONT OF MIND</h3><p>There's nothing more frustrating than having us tell you what to do. At Velmora Flowers you are first and we're here to guide you on your floral journey.</p></article>
        <article class="reason"><h3>WE HAVE MAGIC</h3><p>When creating floral designs it's never easy to get it right the first time, that's why we always do mockups before the final piece. This is why each and every one of our creations are different and unique.</p></article>
      </div>
      <div>
        <article class="reason"><h3>WE LOVE THE DETAIL</h3><p>Creating floral bouquets isn't easy and always adds the element of challenge. Making a meaningful floral bouquet means building detail into it. That's us, we love the little things that make it personal.</p></article>
        <article class="reason"><h3>WE'RE RESPONSIBLE</h3><p>We're kind to the earth. Where possible we try not to use floral foam (the oasis foam you find in floral arrangements). We're developing new ways of arrangement that's better for the environment.</p></article>
        <article class="reason"><h3>WE'RE FRIENDLY</h3><p>It's smiles all round at Velmora Flowers. They say it isn't a job when you enjoy what you do. This is why we at Velmora Flowers are always happy to help, no matter how big or small the event. It's smiles all round, and we are always happy to help.</p></article>
      </div>
    </div>
  </section>

  <footer class="footer">
    <p class="contact contact--email"><svg viewBox="0 0 16 16"><rect x="1" y="3" width="14" height="10" fill="#1a1a1a"/><path d="M1 3l7 6 7-6" fill="none" stroke="#eaa5ca" stroke-width="1.2"/></svg>contactus@velmoraflowers.com.au</p>
    <p class="contact contact--phone"><svg viewBox="0 0 16 16"><path d="M3 1.5l3 .5 1 3.5-2 1.2c.8 1.8 2.2 3.2 4 4l1.2-2 3.5 1 .5 3c-.6.8-1.6 1.3-2.6 1.3C6.5 13.7 2.3 9.5 1.8 4.3 1.7 3.1 2.2 2.1 3 1.5z" fill="#1a1a1a"/></svg>+61 4 782 150 96</p>
    <p class="web"><svg viewBox="0 0 16 16" fill="none" stroke="#fff" stroke-width="1.2"><circle cx="8" cy="8" r="6.5"/><ellipse cx="8" cy="8" rx="3" ry="6.5"/><line x1="1.5" y1="8" x2="14.5" y2="8"/></svg>www.velmoraflowers.com.au</p>
  </footer>
</main>
</body>
</html>
```